Flyer Dachdeckerhandwerk
Zielgruppe
Die Steilhang- und Kieselwerk GmbH ist ein renommiertes, inhabergeführtes Familienunternehmen im Dachdeckerhandwerk. Seit über 30 Jahren stehen wir für höchste Qualität, Zuverlässigkeit und fachgerechte Ausführung – von der ersten Beratung bis zur termintreuen Umsetzung auf der Baustelle. Unsere Kunden profitieren von fundiertem Know-how, eingespielten Abläufen und einem starken Team, das langlebige und wirtschaftliche Lösungen realisiert.
Wir bieten eine begrenzte Aktion an und bieten bis 30.06.2026 eine kostenfreie Dachinspektion.
Die Kunden sollen hierfür bei uns anrufen, oder eine Mail mit dem Betreff 'Dachinspektion 2026' senden.
Aufgabenstellung
Unser CI laden wir hoch.
Es soll modern aussehen.

```html
<!DOCTYPE html>
<html lang="de">
<head>
<meta charset="utf-8">
<title>S&amp;K Steilhang- und Kieselwerk GmbH – Kostenfreie Dachinspektion</title>
<link href="https://fonts.googleapis.com/css2?family=Fira+Sans+Condensed:ital,wght@0,300;0,400;0,600;0,700;1,300&family=Fira+Sans+Extra+Condensed:wght@700;800&display=swap" rel="stylesheet">
<style>
  :root{
    --green:#009a4a;
    --green-soft:#12a553;
    --dark:#0d3f28;
    --ink:#0d3f28;
    --grey:#ebebeb;
    --white:#ffffff;
  }
  *{margin:0;padding:0;box-sizing:border-box}
  html,body{width:848px;height:1200px;overflow:hidden;background:var(--white)}
  body{position:relative;font-family:"Fira Sans Condensed",sans-serif;color:#1a1a1a}

  .hero{position:absolute;left:0;top:0;width:848px;height:334px;
    background:linear-gradient(100deg,#0b2d1c 0%,#0f3d26 35%,#176b40 65%,#2f9a5f 100%)}
  .brand{position:absolute;left:68px;top:33px;display:flex;align-items:center;gap:10px;color:var(--white)}
  .brand-square{width:40px;height:40px;background:var(--white)}
  .brand-name{font-size:22px;line-height:23px;font-weight:400}
  .offer-badge{position:absolute;left:620px;top:34px;width:160px;height:28px;background:var(--green);
    color:var(--white);font-weight:600;font-size:15px;display:flex;align-items:center;justify-content:center;gap:6px}
  .kicker{position:absolute;left:68px;top:121px;color:var(--green);font-weight:700;font-size:15px;letter-spacing:3.2px}
  .headline{position:absolute;left:66px;top:138px;font-family:"Fira Sans Extra Condensed",sans-serif;font-weight:800;
    font-size:62px;line-height:62px;color:var(--white)}
  .headline .accent{color:var(--green)}

  .offer-band{position:absolute;left:0;top:334px;width:848px;height:114px;background:var(--green);color:var(--white)}
  .offer-title{position:absolute;left:67px;top:38px;font-weight:700;font-size:28px}
  .offer-sub{position:absolute;left:67px;top:70px;font-size:15px;font-weight:400}
  .deadline{position:absolute;left:701px;top:18px;width:79px;height:79px;background:var(--dark);text-align:right;padding:12px 6px 0 0}
  .deadline small{display:block;font-size:12px;font-weight:300}
  .deadline strong{display:block;font-size:20px;line-height:20px;font-weight:700;margin-top:4px}

  .intro{position:absolute;left:68px;top:470px;width:712px;border-left:4px solid var(--green);padding-left:18px;
    font-size:13.3px;line-height:19px;color:var(--ink)}

  .services{position:absolute;left:68px;top:527px;width:712px;display:flex;justify-content:space-between}
  .service{width:195px;height:90px;background:var(--grey);border-top:3px solid var(--green);padding:10px 9px}
  .service h3{font-size:14px;font-weight:600;color:var(--ink);letter-spacing:.4px;margin-bottom:5px}
  .service p{font-size:11px;line-height:15.5px;color:var(--ink)}

  .project{position:absolute;top:637px;width:308px;height:165px}
  .project.left{left:68px}.project.right{left:472px}
  .project-photo{width:308px;height:143px;background:linear-gradient(120deg,#24262a 0%,#3a3d42 45%,#6b6f73 75%,#9aa0a2 100%)}
  .project.right .project-photo{background:linear-gradient(240deg,#24262a 0%,#3a3d42 45%,#6b6f73 75%,#a4a8ab 100%)}
  .project-caption{height:22px;background:var(--dark);color:var(--white);font-weight:600;font-size:12.5px;
    display:flex;align-items:center;justify-content:center}

  .facts{position:absolute;left:68px;top:827px;width:712px;height:90px;background:var(--dark);display:flex;align-items:center}
  .fact{flex:1;height:64px;display:flex;flex-direction:column;align-items:center;justify-content:center;color:var(--green-soft)}
  .fact + .fact{border-left:3px solid var(--green)}
  .fact b{font-size:28px;line-height:28px;font-weight:700}
  .fact span{font-size:9.5px;line-height:9px;font-weight:300}
  .fact svg{margin-bottom:6px}

  .steps{position:absolute;left:68px;top:942px;width:712px;height:174px;border:4px solid var(--dark)}
  .steps h2{position:absolute;left:6px;top:6px;font-size:19.5px;font-weight:600;color:var(--ink)}
  .step{position:absolute;top:40px;width:190px}
  .step:nth-of-type(1){left:30px}.step:nth-of-type(2){left:249px}.step:nth-of-type(3){left:468px}
  .step-num{position:absolute;left:0;top:2px;width:19px;height:19px;border-radius:50%;background:var(--green);color:var(--white);
    font-size:12px;font-weight:600;display:flex;align-items:center;justify-content:center}
  .step h4{margin-left:25px;font-size:12.5px;font-weight:600;color:var(--ink)}
  .step p{margin-left:25px;font-size:9.5px;line-height:13.5px;color:var(--ink);margin-top:3px}
  .rule{position:absolute;left:13px;top:102px;width:678px;height:3px;background:var(--green)}
  .contacts{position:absolute;left:13px;top:112px;width:678px;display:flex;justify-content:space-between}
  .contact{width:218px;height:46px;background:var(--green);color:var(--white);padding:7px 15px}
  .contact small{display:block;font-size:11px;font-weight:400;letter-spacing:.3px}
  .contact strong{display:block;font-size:16px;font-weight:600;line-height:18px}

  .footer{position:absolute;left:0;top:1165px;width:848px;height:35px;background:var(--dark);color:var(--green);
    display:flex;align-items:center;justify-content:space-between;padding:0 68px;font-size:11px;font-weight:300}
  .footer em{font-style:italic}
</style>
</head>
<body>
  <header class="hero" role="img" aria-label="Foto: moderne Dachgauben mit Schieferverkleidung und kahlen Bäumen, grün eingefärbt">
    <div class="brand">
      <div class="brand-square"></div>
      <div class="brand-name">Steilhang- und<br>Kieselwerk GmbH</div>
    </div>
    <div class="offer-badge">
      <svg width="13" height="11" viewBox="0 0 13 11"><path d="M1 6l4 4 7-9" fill="none" stroke="#fff" stroke-width="2"/></svg>
      Aktionsangebot 2026
    </div>
    <div class="kicker">KOSTENLOSE DACHINSPEKTION</div>
    <h1 class="headline">IHR DACH.<br><span class="accent">UNSER</span> ZUHAUSE.</h1>
  </header>

  <section class="offer-band">
    <div class="offer-title">Kostenfreie Dachinspektion — Jetzt sichern!</div>
    <div class="offer-sub">Professionelle Begutachtung durch erfahrene Dachdecker — ohne Verpflichtung.</div>
    <div class="deadline"><small>Nur bis</small><strong>30. Juni<br>2026</strong></div>
  </section>

  <p class="intro">Seit über <b>30 Jahren</b> realisieren wir hochwertige Flachdachlösungen in Mainz-Kastel und Umgebung. Mit einem eingespielten Team, hochwertigen Materialien und termingerechter Umsetzung — vom privaten Wohnbau bis zur Großbaustelle.</p>

  <section class="services">
    <article class="service"><h3>FLACHDACH</h3><p>Planung, Abdichtung und Sanierung aller Flachdachsysteme — langlebig und wirtschaftlich.</p></article>
    <article class="service"><h3>BEGRÜNUNG</h3><p>Extensiv- und Intensivbegrünung für nachhaltige, wärmedämmende Dachlösungen.</p></article>
    <article class="service"><h3>WARTUNG &amp; INSPEKTION</h3><p>Regelmäßige Begehung und Dokumentation — für ein sicheres Dach das ganze Jahr.</p></article>
  </section>

  <figure class="project left">
    <div class="project-photo" role="img" aria-label="Foto: Zinkdach mit Gauben in Mainz-Kastel"></div>
    <figcaption class="project-caption">Zinkdach — Mainz-Kastel</figcaption>
  </figure>
  <figure class="project right">
    <div class="project-photo" role="img" aria-label="Foto: Schiefer- und Flachdach mit Gauben in Frankfurt"></div>
    <figcaption class="project-caption">Schiefer &amp; Flachdach — Frankfurt</figcaption>
  </figure>

  <section class="facts">
    <div class="fact"><b>30+</b><span>Jahre</span><span>Erfahrung</span></div>
    <div class="fact"><b>100%</b><span>Familienbetrieb</span></div>
    <div class="fact"><svg width="30" height="22" viewBox="0 0 30 22"><path d="M2 11l9 9L28 2" fill="none" stroke="#12a553" stroke-width="5"/></svg><span>Meisterbetrieb</span></div>
    <div class="fact"><svg width="30" height="22" viewBox="0 0 30 22"><path d="M2 11l9 9L28 2" fill="none" stroke="#12a553" stroke-width="5"/></svg><span>Termintreue</span></div>
  </section>

  <section class="steps">
    <h2>So einfach geht's — Dachinspektion anfragen:</h2>
    <div class="step"><div class="step-num">1</div><h4>Anrufen</h4><p>Kurz Bescheid geben — wir vereinbaren einen Termin.</p></div>
    <div class="step"><div class="step-num">2</div><h4>E-Mail senden</h4><p>Betreff: <b>„Dachinspektion 2026"</b> — wir melden uns innerhalb von 24 Std.</p></div>
    <div class="step"><div class="step-num">3</div><h4>Kostenlos prüfen lassen</h4><p>Unsere Experten kommen zu Ihnen — unverbindlich &amp; kostenlos.</p></div>
    <div class="rule"></div>
    <div class="contacts">
      <div class="contact"><small>TELEFEN</small><strong>JETZT ANRUFEN</strong></div>
      <div class="contact"><small>E-MAIL</small><strong>info@suk-kieselwerk.de</strong></div>
      <div class="contact"><small>WEBSITE</small><strong>www.suk-kieselwerk.de</strong></div>
    </div>
  </section>

  <footer class="footer">
    <span>S&amp;K Steilhang- und Kieselwerk GmbH · Mainz-Kastel</span>
    <em>Denn das Dach ist unser Zuhause.</em>
  </footer>
</body>
</html>
```